DVR Conference Newsletter Postcard

We need a template design for a direct mailer postcard that we are sending to potential attendees. The attached templates include the dimensions of the postcard. It is a panel/map type of postcard so it has 8 surfaces that need to have content on them. The purpose of this project is to get people to sign up and attend our conference in May. I have attached what type of layout we would like to have on each panel of the postcard.

Target Market(s)

Category Managers, Shopper Insights, Shopper Marketing

Industry/Entity Type

Consumer

Font styles to use
Sans Serif

Requirements
Must have
• A fun but clean template that includes designs, graphics, elements that show lists, our agenda, pop up graphics that can show facts and stats.
• An interesting shopper cart graphic that include insights, analytics, data, networking, etc.
Nice to have
• Maybe some fun content based on the conference title.
Should not have
• No animated characters. We want this to be clean and innovative, but fun.

```html
<!DOCTYPE html>
<html lang="en">
<head>
<meta charset="UTF-8">
<title>DVR Conference Postcard – Front Cover</title>
<link href="https://fonts.googleapis.com/css2?family=Montserrat:wght@600;700&family=Questrial&display=swap" rel="stylesheet">
<style>
  :root {
    --page-bg: #eef1f4;
    --card-white: #ffffff;
    --card-tint: #e6f1f8;
    --navy-teal: #0f5f86;
    --band-teal: #0e6a8c;
    --sky: #1ea6da;
    --sky-light: #42b9e8;
    --ink-grey: #3c4a55;
    --rule: #1ea6da;
  }
  * { margin: 0; padding: 0; box-sizing: border-box; }
  html, body {
    width: 1200px;
    height: 900px;
    overflow: hidden;
    background: var(--page-bg);
  }
  .postcard {
    position: absolute;
    left: 168px;
    top: 170px;
    width: 866px;
    height: 560px;
    background: linear-gradient(150deg, var(--card-white) 45%, var(--card-tint) 100%);
    border: 1px solid #d3dbe2;
    overflow: hidden;
  }
  .headline {
    position: absolute;
    left: 40px;
    top: 74px;
    width: 245px;
    text-align: right;
  }
  .headline-strong {
    font-family: "Montserrat", sans-serif;
    font-weight: 700;
    font-size: 29px;
    line-height: 33px;
    color: var(--navy-teal);
    letter-spacing: 0.2px;
  }
  .headline-light {
    font-family: "Questrial", sans-serif;
    font-size: 29px;
    line-height: 33px;
    color: var(--sky);
    letter-spacing: 2.4px;
  }
  .headline-rule {
    position: absolute;
    left: 317px;
    top: 62px;
    width: 2px;
    height: 220px;
    background: var(--rule);
  }
  .hero-art {
    position: absolute;
    left: 360px;
    top: 65px;
    width: 390px;
    height: 212px;
    border-radius: 6px;
    background:
      radial-gradient(circle at 32% 48%, #0d5f94 0, #1679b3 22%, rgba(60,170,220,0.85) 40%, rgba(150,215,240,0.5) 70%, rgba(220,240,250,0) 100%);
  }
  .event-info {
    position: absolute;
    left: 447px;
    top: 332px;
  }
  .event-name {
    font-family: "Montserrat", sans-serif;
    font-weight: 600;
    font-size: 19px;
    line-height: 31px;
    color: var(--sky-light);
    text-transform: uppercase;
  }
  .event-venue {
    margin-top: 14px;
    font-family: "Questrial", sans-serif;
    font-size: 14.5px;
    letter-spacing: 1.2px;
    color: var(--ink-grey);
    text-transform: uppercase;
  }
  .event-dates {
    margin-top: 3px;
    font-family: "Montserrat", sans-serif;
    font-weight: 700;
    font-size: 16px;
    color: var(--navy-teal);
    text-transform: uppercase;
  }
  .register-band {
    position: absolute;
    left: 445px;
    top: 462px;
    right: 0;
    height: 23px;
    background: var(--band-teal);
    padding-left: 8px;
    font-family: "Questrial", sans-serif;
    font-size: 16px;
    line-height: 23px;
    color: #7fd2f2;
  }
  .register-link {
    position: absolute;
    left: 453px;
    top: 486px;
    font-family: "Questrial", sans-serif;
    font-size: 16.5px;
    line-height: 21px;
    color: var(--sky-light);
    letter-spacing: 0.3px;
  }
  .register-link strong {
    font-family: "Montserrat", sans-serif;
    font-weight: 700;
    font-size: 15.5px;
    color: var(--navy-teal);
  }
</style>
</head>
<body>
  <main class="postcard">
    <h1 class="headline">
      <span class="headline-strong">BRIDGING<br>TRADITIONAL<br>&amp; DIGITAL:</span><br>
      <span class="headline-light">CREATING<br>NEW PATHS<br>TO SUCCESS</span>
    </h1>
    <div class="headline-rule"></div>
    <div class="hero-art" role="img" aria-label="Shopping cart emblem in a blue circle surrounded by floating translucent blue tiles with small retail icons such as a delivery van, phone, tablet and shopping bag"></div>

    <section class="event-info">
      <h2 class="event-name">Category Management &amp;<br>Shopper Insights Conference</h2>
      <p class="event-venue">Meridian Grand Hotel, Las Vegas, NV</p>
      <p class="event-dates">May 15th – May 17th, 2017</p>
    </section>

    <div class="register-band">Register Here:</div>
    <p class="register-link">http://<strong>dvrconf.events</strong>/events/<br>annual-conference/registration</p>
  </main>
</body>
</html>
```